Executive Coach needs elegant business card design

I need a business card design which includes following info: name, email (same as name, @quillpost.com), phone. I'd put that on one side. On the other side i'd like some graphic indicating what i do:
- using questions to help people get great results
- encourage people to try different solutions to overcome old problems
- untangling the mental knot that traps people in vicious circles
- question mental models to get people to see a different point of view.

I'd like an elegant design. Bonus points for providing a different twist on things. I've included 2 designs I started with. Feel free to improve or discard them :-)

```html
<!DOCTYPE html>
<html lang="en">
<head>
<meta charset="utf-8">
<title>Daniel Hartley – Business Card</title>
<link rel="stylesheet" href="https://fonts.googleapis.com/css2?family=Oswald:wght@300;400&display=swap">
<style>
  :root {
    --navy: #34448a;
    --indigo: #5367a8;
    --steel: #6f93c8;
    --sky: #9dc2e8;
    --paper: #f1f1f1;
    --tile: #ececec;
    --stone: #cbc8ca;
    --ink: #3d3d40;
    --pale-text: #a9c8ee;
    --mid-text: #4a5fa0;
    --icon: #8aa6c9;
    --page: #e9e6e2;
  }
  * { box-sizing: border-box; margin: 0; padding: 0; }
  html, body { width: 1200px; height: 1000px; overflow: hidden; }
  body {
    background: var(--page);
    position: relative;
    font-family: "Oswald", sans-serif;
  }
  .card {
    position: absolute;
    width: 700px;
    height: 400px;
    box-shadow: 0 6px 18px rgba(0,0,0,.18);
    overflow: hidden;
  }

  /* Contact side */
  .card--contact { left: 440px; top: 60px; background: var(--paper); }
  .colour-strip { position: absolute; left: 0; top: 0; width: 110px; height: 100%; display: flex; flex-direction: column; }
  .colour-strip span { flex: 1; }
  .colour-strip .s1 { background: var(--navy); }
  .colour-strip .s2 { background: var(--indigo); }
  .colour-strip .s3 { background: var(--steel); }
  .colour-strip .s4 { background: var(--sky); }
  .footer-band { position: absolute; left: 110px; right: 0; bottom: 0; height: 95px; background: var(--stone); }
  .holder-name {
    position: absolute; right: 28px; top: 58px;
    font-size: 46px; font-weight: 400; color: var(--ink); letter-spacing: 1px;
  }
  .name-rule { position: absolute; left: 150px; right: 18px; top: 122px; height: 1px; background: var(--ink); }
  .contact-line {
    position: absolute; right: 30px;
    display: flex; align-items: center; gap: 14px;
    font-size: 36px; font-weight: 400; color: var(--ink); letter-spacing: .5px;
  }
  .contact-line--email { top: 150px; }
  .contact-line--phone { top: 230px; }

  /* Message side */
  .card--message { left: 70px; top: 520px; background: var(--tile); }
  .row { position: absolute; left: 0; width: 700px; height: 100px; }
  .row--1 { top: 0; } .row--2 { top: 100px; } .row--3 { top: 200px; } .row--4 { top: 300px; }
  .band {
    position: absolute; top: 0; height: 100px;
    display: flex; align-items: center; justify-content: center;
    font-size: 34px; font-weight: 300; letter-spacing: .5px; white-space: nowrap;
  }
  .band .q { text-transform: uppercase; }
  .band .divider { width: 1px; height: 60px; margin: 0 16px; opacity: .6; background: currentColor; }
  .band--navy { left: 0; width: 560px; background: var(--navy); color: var(--pale-text); }
  .band--indigo { left: 140px; width: 560px; background: var(--indigo); color: var(--pale-text); }
  .band--steel { left: 0; width: 560px; background: var(--steel); color: var(--mid-text); }
  .band--sky { left: 140px; width: 560px; background: var(--sky); color: var(--navy); font-weight: 400; }
  .tile { position: absolute; top: 0; width: 140px; height: 100px; display: flex; align-items: center; justify-content: center; background: var(--tile); }
  .tile--right { left: 560px; }
  .tile--left { left: 0; }
</style>
</head>
<body>

<section class="card card--contact" aria-label="Contact side">
  <div class="colour-strip"><span class="s1"></span><span class="s2"></span><span class="s3"></span><span class="s4"></span></div>
  <div class="footer-band"></div>
  <h1 class="holder-name">DANIEL Hartley</h1>
  <div class="name-rule"></div>
  <p class="contact-line contact-line--email">
    <svg width="54" height="44" viewBox="0 0 54 44" aria-hidden="true">
      <rect x="3" y="12" width="48" height="30" fill="none" stroke="var(--icon)" stroke-width="2"/>
      <path d="M3 12 L27 2 L51 12" fill="none" stroke="var(--icon)" stroke-width="2"/>
      <path d="M3 42 L22 26 M51 42 L32 26 M3 12 L27 30 L51 12" fill="none" stroke="var(--icon)" stroke-width="2"/>
      <text x="27" y="21" font-size="12" text-anchor="middle" fill="var(--icon)" font-family="sans-serif">@</text>
    </svg>
    danielhartley@quillpost.com
  </p>
  <p class="contact-line contact-line--phone">
    <svg width="28" height="48" viewBox="0 0 28 48" aria-hidden="true">
      <rect x="2" y="2" width="24" height="44" rx="4" fill="none" stroke="var(--icon)" stroke-width="2.5"/>
      <rect x="6" y="7" width="16" height="14" fill="var(--icon)"/>
      <g fill="var(--icon)">
        <rect x="6" y="25" width="4" height="3"/><rect x="12" y="25" width="4" height="3"/><rect x="18" y="25" width="4" height="3"/>
        <rect x="6" y="31" width="4" height="3"/><rect x="12" y="31" width="4" height="3"/><rect x="18" y="31" width="4" height="3"/>
        <rect x="6" y="37" width="4" height="3"/><rect x="12" y="37" width="4" height="3"/><rect x="18" y="37" width="4" height="3"/>
      </g>
    </svg>
    0800.555.0142
  </p>
</section>

<section class="card card--message" aria-label="Message side">
  <div class="row row--1">
    <div class="band band--navy"><span class="q">Tired of treat?</span><span class="divider"></span><span>We can help you!!!</span></div>
    <div class="tile tile--right">
      <svg width="80" height="80" viewBox="0 0 80 80" aria-label="Question icon" role="img">
        <circle cx="40" cy="40" r="36" fill="none" stroke="#111" stroke-width="3"/>
        <text x="40" y="56" font-size="44" text-anchor="middle" fill="#111" font-family="Oswald, sans-serif" font-weight="300">?</text>
      </svg>
    </div>
  </div>
  <div class="row row--2">
    <div class="tile tile--left">
      <svg width="80" height="80" viewBox="0 0 80 80" aria-label="Upward icon" role="img">
        <circle cx="40" cy="40" r="36" fill="none" stroke="#111" stroke-width="3"/>
        <path d="M24 48 L40 30 L56 48" fill="none" stroke="#111" stroke-width="3.5" stroke-linecap="round" stroke-linejoin="round"/>
      </svg>
    </div>
    <div class="band band--indigo"><span class="q">Problems from past?</span><span class="divider"></span><span>Overcome</span></div>
  </div>
  <div class="row row--3">
    <div class="band band--steel"><span class="q">Vicious circles?</span><span class="divider"></span><span>You can defeat them</span></div>
    <div class="tile tile--right">
      <svg width="90" height="90" viewBox="0 0 90 90" aria-label="Cycle icon" role="img">
        <path d="M15 40 A30 30 0 0 1 72 30" fill="none" stroke="#111" stroke-width="3"/>
        <path d="M64 30 L74 32 L76 22" fill="none" stroke="#111" stroke-width="3"/>
        <path d="M75 50 A30 30 0 0 1 18 60" fill="none" stroke="#111" stroke-width="3"/>
        <path d="M26 60 L16 58 L14 68" fill="none" stroke="#111" stroke-width="3"/>
      </svg>
    </div>
  </div>
  <div class="row row--4">
    <div class="tile tile--left">
      <svg width="96" height="90" viewBox="0 0 96 90" aria-label="Person with choice arrows icon" role="img">
        <g stroke="#111" stroke-width="2.5" fill="none" stroke-linecap="round">
          <path d="M48 24 L48 6 M42 12 L48 6 L54 12"/>
          <path d="M30 44 L8 44 M14 38 L8 44 L14 50"/>
          <path d="M66 44 L88 44 M82 38 L88 44 L82 50"/>
        </g>
        <circle cx="48" cy="40" r="11" fill="#111"/>
        <path d="M28 80 Q28 56 48 56 Q68 56 68 80 Z" fill="#111"/>
      </svg>
    </div>
    <div class="band band--sky"><span class="q">Mired?</span><span class="divider"></span><span>Find different solutions</span></div>
  </div>
</section>

</body>
</html>
```